Texas Civic Builders Summit Needs a Flyer

One-page event graphic/flyer and header needed. Logos provided.

2023 Texas Civic Builders Summit
Bold Ventures – True Accounts, True Answers, True Wins
August 10-11, 2023
San Antonio, Texas

About the Forum:
“Capital projects are full of risk. It’s not a question of eliminating risk, it’s a question of how to clearly identify it, reduce it, change it, or battle it.”
- Denise Holmgarten, Founder, U-BraMQ; Civic Design Advisor

Real Stories, Real Solutions, Real Success: U-BraMQ’s Texas Civic Builders Summit (TCBS) is designed to help you attain project success by hearing from Public Project Owners, architects, engineers, consultants, contractors, and suppliers. We are all in this together, and U-BraMQ is the organization that champions cross-collaboration and communication for project success!

For reference in design ONLY -
Here are some topic areas that bring project risks and/or rewards and that ultimately affect the Public Project Owner’s project success:

• Project Planning
• Regional Growth Shifts
• Project Funding
• Contracting
• Governmental Regulations
• Long-term COVID Impacts
• Infrastructure and Site Design
• Safety and Security
• Sustainability and Resilience
• Construction Predictability
• Leveraging Technology
• Facility Operations

Target Market(s)

Architects, Engineers, Contractors, project owners

Industry/Entity Type

Design and Construction

Requirements
Must have
• This is for a one-page (8.5x11) event graphic/flyer only - logos are provided. U-BraMQ logo, Texas Civic Builders Summit (TCBS) logo, 2023 Texas Civic Builders Summit, date, location
Nice to have
• Graphic(s) that represent the design and construction industry and the theme of this event (title, topics covered)
Should not have
• Full project description

```html
<!DOCTYPE html>
<html lang="en">
<head>
<meta charset="utf-8">
<title>2023 Texas Civic Builders Summit – Flyer</title>
<link rel="stylesheet" href="https://fonts.googleapis.com/css2?family=Oswald:wght@400;500;600&family=Roboto:wght@900&family=Roboto+Condensed:wght@400;700&display=swap">
<style>
  :root{
    --navy:#2e3b93;
    --green:#8fb52f;
    --green-dark:#6f8f1f;
    --ink:#222;
    --muted:#555;
    --paper:#ffffff;
    --backdrop:#eeeeee;
  }
  *{box-sizing:border-box;margin:0;padding:0}
  html,body{width:1200px;height:840px;overflow:hidden;background:var(--backdrop)}
  body{display:flex;align-items:center;justify-content:center;font-family:"Roboto Condensed",sans-serif;color:var(--ink)}

  .flyer{position:relative;width:566px;height:800px;background:var(--paper);box-shadow:0 4px 18px rgba(0,0,0,.12)}

  /* left column */
  .main{position:absolute;left:0;top:0;width:288px;height:800px}
  .brand{height:91px;display:flex;align-items:center;gap:10px;padding-left:44px}
  .brand-mark{width:14px;height:14px;background:var(--green)}
  .brand-name{font-family:"Roboto Condensed",sans-serif;font-weight:700;font-size:26px;color:var(--green-dark);text-transform:uppercase;letter-spacing:2px}
  .hero{width:288px;height:211px;background:linear-gradient(180deg,#f0b247 0%,#c9a36a 28%,#8a8f8a 55%,#5f6a63 80%,#4a5550 100%)}

  .event{padding-left:43px;width:288px}
  .event-year{margin-top:19px;width:195px;font-family:"Oswald",sans-serif;font-weight:500;font-size:27px;line-height:31px;color:var(--navy);text-align:center}
  .event-sub{width:195px;display:flex;align-items:center;gap:6px;font-family:"Oswald",sans-serif;font-weight:500;font-size:20px;line-height:22px;color:var(--green)}
  .event-sub::before,.event-sub::after{content:"";flex:1;height:2px;background:var(--navy)}
  .theme-big{margin-top:10px;width:195px;font-family:"Roboto",sans-serif;font-weight:900;font-size:70px;line-height:58px;color:var(--navy);text-align:center;letter-spacing:1px}
  .theme-word{width:195px;font-family:"Oswald",sans-serif;font-weight:500;font-size:28px;line-height:32px;color:var(--green);letter-spacing:10.5px}
  .theme-tag{font-weight:700;font-size:9.6px;color:var(--ink);margin-top:2px}

  .dates{margin-top:15px;width:195px;display:grid;grid-template-columns:60px 133px;grid-template-rows:52px 53px;gap:2px;font-family:"Oswald",sans-serif;font-weight:500}
  .dates span{display:flex;align-items:center;justify-content:center;color:#fff}
  .day{background:var(--green);font-size:38px}
  .month{background:var(--navy);font-size:38px}
  .year{background:var(--navy);font-size:44px}

  .venue{margin-top:9px;display:flex;align-items:center;gap:4px;font-family:"Oswald",sans-serif;font-weight:500;font-size:25px;color:var(--navy)}
  .venue b{color:var(--green);font-weight:500}

  .about{width:195px;text-align:center}
  .about-title{margin-top:13px;font-family:"Oswald",sans-serif;font-weight:500;font-size:13px;color:var(--green)}
  .quote{margin-top:6px;border-top:1px solid var(--navy);border-bottom:1px solid var(--navy);padding:9px 2px 8px;font-size:8.4px;line-height:10.6px;color:var(--ink);position:relative}
  .quote::before,.quote::after{position:absolute;left:50%;transform:translateX(-50%);background:#fff;padding:0 3px;color:var(--green);font-size:12px;font-weight:700;line-height:8px}
  .quote::before{content:"\201C";top:-4px}
  .quote::after{content:"\201D";bottom:-5px}
  .credit{margin-top:9px;font-size:8px;line-height:10.5px;color:var(--muted)}
  .credit .name{color:var(--navy)}
  .credit .role{color:var(--green-dark)}
  .url{position:absolute;left:43px;bottom:0;width:195px;height:23px;background:var(--navy);color:#fff;font-size:12px;display:flex;align-items:center;justify-content:center}

  /* right column */
  .side{position:absolute;left:288px;top:0;width:264px}
  .panel{background:var(--navy);height:564px;position:relative;padding:20px 18px 0 27px;color:#fff}
  .panel::before{content:"";position:absolute;left:16px;top:24px;bottom:24px;width:1px;background:var(--green)}
  .note{position:relative;font-size:10px;line-height:13px;text-align:justify;margin-bottom:14px}
  .note::before{content:"";position:absolute;left:-13.5px;top:3px;width:6px;height:6px;border-radius:50%;background:var(--green);box-shadow:0 0 0 1.5px var(--navy)}
  .ribbon{position:relative;margin:6px -27px 18px -36px;height:30px;background:var(--green);display:flex;align-items:center;justify-content:center;font-family:"Oswald",sans-serif;font-weight:500;font-size:12.5px;z-index:1}
  .topics{background:var(--green);height:218px;list-style:none;padding:15px 0 0 27px}
  .topics li{display:flex;align-items:center;gap:7px;font-size:10.8px;line-height:16px;color:#fff}
  .topics svg{flex:none}
</style>
</head>
<body>
  <article class="flyer">
    <section class="main">
      <header class="brand">
        <span class="brand-mark"></span>
        <span class="brand-name">U-BraMQ</span>
      </header>
      <div class="hero" role="img" aria-label="Aerial photo of a downtown skyline with parking lots at golden sunset"></div>

      <div class="event">
        <h1 class="event-year">2023 TEXAS CIVIC</h1>
        <p class="event-sub">BUILDERS SUMMIT</p>
        <p class="theme-big">BOLD</p>
        <p class="theme-word">VENTURES</p>
        <p class="theme-tag">True Accounts, True Answers, True Wins</p>

        <div class="dates">
          <span class="day">10</span><span class="month">AUGUST</span>
          <span class="day">11</span><span class="year">2023</span>
        </div>

        <p class="venue">
          <svg width="12" height="17" viewBox="0 0 12 17" aria-hidden="true"><path d="M6 0a6 6 0 0 0-6 6c0 4.5 6 11 6 11s6-6.5 6-11a6 6 0 0 0-6-6z" fill="#2e3b93"/><circle cx="6" cy="6" r="2.3" fill="#8fb52f"/></svg>
          SAN ANTONIO, <b>TEXAS</b>
        </p>

        <div class="about">
          <h2 class="about-title">ABOUT THE FORUM:</h2>
          <blockquote class="quote">Capital projects are full of risk. It's not a question of eliminating risk, it's a question of how to clearly identify it, reduce it, change it, or battle it.</blockquote>
          <p class="credit"><span class="name">Denise Holmgarten,</span> <span class="role">Founder, U-BraMQ;</span><br>Civic Design Advisor</p>
        </div>
      </div>
      <p class="url">www.u-bramq.example.org</p>
    </section>

    <aside class="side">
      <div class="panel">
        <p class="note">Each of us have impressive stories of how, when faced with a project situation, we or our teams have overcome challenges and found project rewards through novel solutions, making lemonade out of lemons, or just taking steps forward through the muck and mire. If only we could better identify those risks in advance and be able to mitigate them early. After all, “Failure is not an option!”</p>
        <p class="note">Most of the project issues we encounter are ones we have already experienced, or ones that other Public Project Owners or their AEC teams have experienced. The thing is, we often fail to learn from those experiences, fail to act in advance to mitigate them, do not know what to do, or feel powerless to make change. Plus, new risks pop up on every project and shift from project inception through operations!</p>
        <p class="note">You can't eliminate all risk from your project and there's no way to control for all potential risks but thinking through them ahead of time can save you and your project from failure, and even bring rewards.</p>
        <h2 class="ribbon">REAL STORIES, REAL SOLUTIONS, REAL SUCCESS:</h2>
        <p class="note">U-BraMQ's Texas Civic Builders Summit (TCBS) is designed to help you attain project success by hearing from Public Project Owners, architects, engineers, consultants, contractors, and suppliers. We are all in this together, and U-BraMQ is the organization that champions cross-collaboration and communication for project success!</p>
        <p class="note">With a limited attendance, THIS IS YOUR OPPORTUNITY to experience an intimate, safe environment where project pains and triumphs, challenges and solutions, risks and rewards, are shared openly.</p>
      </div>
      <ul class="topics">
        <li><svg width="8" height="8" viewBox="0 0 8 8"><rect x=".5" y=".5" width="7" height="7" fill="none" stroke="#fff"/><path d="M1.5 4l2 2 4-5" fill="none" stroke="#fff"/></svg>Project Planning</li>
        <li><svg width="8" height="8" viewBox="0 0 8 8"><rect x=".5" y=".5" width="7" height="7" fill="none" stroke="#fff"/><path d="M1.5 4l2 2 4-5" fill="none" stroke="#fff"/></svg>Regional Growth Shifts</li>
        <li><svg width="8" height="8" viewBox="0 0 8 8"><rect x=".5" y=".5" width="7" height="7" fill="none" stroke="#fff"/><path d="M1.5 4l2 2 4-5" fill="none" stroke="#fff"/></svg>Project Funding</li>
        <li><svg width="8" height="8" viewBox="0 0 8 8"><rect x=".5" y=".5" width="7" height="7" fill="none" stroke="#fff"/><path d="M1.5 4l2 2 4-5" fill="none" stroke="#fff"/></svg>Contracting</li>
        <li><svg width="8" height="8" viewBox="0 0 8 8"><rect x=".5" y=".5" width="7" height="7" fill="none" stroke="#fff"/><path d="M1.5 4l2 2 4-5" fill="none" stroke="#fff"/></svg>Governmental Regulations</li>
        <li><svg width="8" height="8" viewBox="0 0 8 8"><rect x=".5" y=".5" width="7" height="7" fill="none" stroke="#fff"/><path d="M1.5 4l2 2 4-5" fill="none" stroke="#fff"/></svg>Long-term COVID Impacts</li>
        <li><svg width="8" height="8" viewBox="0 0 8 8"><rect x=".5" y=".5" width="7" height="7" fill="none" stroke="#fff"/><path d="M1.5 4l2 2 4-5" fill="none" stroke="#fff"/></svg>Infrastructure and Site Design</li>
        <li><svg width="8" height="8" viewBox="0 0 8 8"><rect x=".5" y=".5" width="7" height="7" fill="none" stroke="#fff"/><path d="M1.5 4l2 2 4-5" fill="none" stroke="#fff"/></svg>Safety and Security</li>
        <li><svg width="8" height="8" viewBox="0 0 8 8"><rect x=".5" y=".5" width="7" height="7" fill="none" stroke="#fff"/><path d="M1.5 4l2 2 4-5" fill="none" stroke="#fff"/></svg>Sustainability and Resilience</li>
        <li><svg width="8" height="8" viewBox="0 0 8 8"><rect x=".5" y=".5" width="7" height="7" fill="none" stroke="#fff"/><path d="M1.5 4l2 2 4-5" fill="none" stroke="#fff"/></svg>Construction Predictability</li>
        <li><svg width="8" height="8" viewBox="0 0 8 8"><rect x=".5" y=".5" width="7" height="7" fill="none" stroke="#fff"/><path d="M1.5 4l2 2 4-5" fill="none" stroke="#fff"/></svg>Leveraging Technology</li>
        <li><svg width="8" height="8" viewBox="0 0 8 8"><rect x=".5" y=".5" width="7" height="7" fill="none" stroke="#fff"/><path d="M1.5 4l2 2 4-5" fill="none" stroke="#fff"/></svg>Facility Operations</li>
      </ul>
    </aside>
  </article>
</body>
</html>
```